Local Roofing Company Billboard Design

We need a billboard design for an 8' x 32' billboard. This billboard would need to be easily readable and stand out well.
I have uploaded a design that we like - simple, readable, and gets the point across. We do NOT want the $1000 off offer included.
We are looking for a black background with white copy so it will stand out. We want the following on the billboard:
Corvella Roofing logo
corvella-roofing-example.com (optional)
555.214.7736 (mandatory)
Photo is optional, depends on how it all lays out
Production file must comply with layout requirements (uploaded).
Target Market(s)
Homeowners
Font styles to use
Other font styles liked:
- match font from logo
Colors
Designer to choose colors to be used in the design.
Requirements
Must have
- Black background, white copy, logo must be large and legible. Colors used must match our logo colors.

```html
<!DOCTYPE html>
<html lang="en">
<head>
<meta charset="utf-8">
<title>Corvella Roofing Billboard</title>
<link rel="stylesheet" href="https://fonts.googleapis.com/css2?family=Arvo:wght@700&family=Lato:wght@400;700&display=swap">
<style>
  :root {
    --page: #ffffff;
    --ink: #000000;
    --blush: #f9ddd4;
    --flame: #e4581b;
    --white: #ffffff;
    --seal-grey: #6d6d6d;
    --photo-light: #e9e8e2;
    --photo-mid: #a9a6a2;
    --photo-dark: #5f5c5c;
  }
  html, body {
    margin: 0;
    width: 1200px;
    height: 493px;
    overflow: hidden;
    background: var(--page);
  }
  .canvas {
    position: relative;
    width: 1200px;
    height: 493px;
  }
  .billboard {
    position: absolute;
    left: 64px;
    top: 107px;
    width: 1079px;
    height: 282px;
    display: block;
  }
  .brand-name {
    font-family: "Arvo", "Roboto Slab", serif;
    font-weight: 700;
    font-size: 86px;
    fill: var(--ink);
  }
  .phone-number {
    font-family: "Lato", Arial, sans-serif;
    font-weight: 700;
    font-size: 90px;
    fill: var(--white);
  }
  .web-address {
    font-family: "Lato", Arial, sans-serif;
    font-weight: 400;
    font-size: 33px;
    fill: var(--white);
  }
</style>
</head>
<body>
<div class="canvas">
  <svg class="billboard" viewBox="137 228 2301 602" xmlns="http://www.w3.org/2000/svg" aria-label="Corvella Roofing billboard">
    <defs>
      <linearGradient id="house-tones" x1="0" y1="0" x2="1" y2="1">
        <stop offset="0" stop-color="var(--photo-light)"/>
        <stop offset="0.55" stop-color="var(--photo-mid)"/>
        <stop offset="1" stop-color="var(--photo-dark)"/>
      </linearGradient>
    </defs>

    <rect class="backdrop" x="137" y="228" width="2301" height="602" fill="var(--ink)"/>

    <polygon class="gable-panel" points="137,515 678,272 1940,830 137,830" fill="var(--blush)"/>
    <polygon class="gable-edge-left" points="137,495 660,262 678,272 137,515" fill="var(--flame)"/>
    <polygon class="gable-edge-right" points="585,228 640,228 1975,830 1935,830" fill="var(--flame)"/>

    <polygon class="house-photo" role="img" aria-label="Photo of a house gable with light siding, shuttered windows and grey shingle roof"
      points="1350,552 1778,255 1930,340 2438,440 2438,830 1978,830" fill="url(#house-tones)"/>

    <polygon class="contact-band" points="137,676 1572,676 1796,775 137,775" fill="var(--ink)"/>
    <polygon class="band-rule-top" points="137,672 1565,672 1578,680 137,680" fill="var(--flame)"/>
    <polygon class="band-rule-bottom" points="137,771 1788,771 1806,779 137,779" fill="var(--flame)"/>

    <circle class="cert-seal" cx="1340" cy="385" r="60" fill="var(--seal-grey)"/>

    <text class="brand-name" x="292" y="622">Corvella Roofing</text>

    <g class="phone-icon" fill="none" stroke="var(--white)" stroke-width="5">
      <circle cx="307" cy="727" r="33"/>
      <path d="M294,708 l8,-3 6,12 -6,5 c3,8 8,13 15,16 l5,-6 12,6 -3,8 c-18,4 -40,-18 -37,-38z" fill="var(--white)" stroke="none"/>
    </g>
    <text class="phone-number" x="356" y="757">555.214.7736</text>

    <g class="globe-icon" fill="none" stroke="var(--white)" stroke-width="3">
      <circle cx="971" cy="729" r="15"/>
      <ellipse cx="971" cy="729" rx="6" ry="15"/>
      <line x1="956" y1="729" x2="986" y2="729"/>
      <line x1="959" y1="721" x2="983" y2="721"/>
      <line x1="959" y1="737" x2="983" y2="737"/>
    </g>
    <text class="web-address" x="994" y="741">corvella-roofing-example.com</text>
  </svg>
</div>
</body>
</html>
```